Copper Lantern Gatherings need a stand out marketing flyer.

Copper Lantern Gatherings is a company that runs empowerment retreats and bespoke corporate training in creating positive change.
We would like an A5 flyer that is 2 sided. the reverse side of the flyer we would like some of our testimonial quotes.

The flyer should be punchy and not too heavy with wordy detail but have enough detail so people can see what we offer. Encouraging people to contact us to find out more

Our empowerment retreats help people to live without limits, be fierce and wild, be creative and courageous, be fearless and free.
Leave behind
- lack of self esteem
- lack of personal power
- lack of focus
- old fears and beliefs
- overwhelm
Find new
- confidence
- personal empowerment
- commitment
- courage
- resilience

Contact details:
website: www.copperlanterngatherings.example.co.uk
email: info@copperlanterngatherings.example.com
Rebecca Thornby Tel: 07700 900 318
Joanna Pelling Tel: 07700 900 752

You can use as much of the detail above in your design as you would like..
I attach our logos. you can pick which ever design you prefer to work with. I have also attached a file that contains the testimonials for the reverse of the slide. I've also attached a few pictures but these aren't necessary in your design they are just an option/idea for you to consider. You can use alternative pictures should you wish to.

Details for our up and coming events can be found on our website

```html
<!DOCTYPE html>
<html lang="en">
<head>
<meta charset="utf-8">
<title>Copper Lantern Gatherings – Flyer</title>
<link rel="stylesheet" href="https://fonts.googleapis.com/css2?family=Space+Mono:wght@400;700&family=Tinos&display=swap">
<style>
:root{
  --page:#232323;
  --blue:#2f7bc8;
  --blue-soft:#3a78bb;
  --navy:#3a5a8e;
  --ink:#ffffff;
  --light:#e9edf1;
  --line:#8d8d8d;
  --quote:#3f7fc0;
  --scene:#a7d8e5;
  --mono:'Space Mono', monospace;
  --serif:'Tinos', serif;
}
html,body{margin:0;padding:0;overflow:hidden;}
body{width:1200px;height:4307px;background:var(--scene);}
.canvas{position:relative;width:1200px;height:4307px;overflow:hidden;font-family:var(--mono);color:var(--ink);}
.page{position:absolute;left:0;width:1200px;background:var(--page);overflow:hidden;}
.page--front{top:0;height:1591px;}
.page--back{top:1701px;height:1599px;}
.decor{position:absolute;left:0;top:0;}
.abs{position:absolute;margin:0;}

.brand{left:40px;top:70px;display:flex;align-items:center;gap:10px;font-size:15px;font-weight:700;color:var(--blue);letter-spacing:1px;}
.brand__dot{width:22px;height:22px;border-radius:50%;background:var(--blue);}

.hero-title{left:87px;top:360px;font-size:64px;font-weight:700;line-height:86px;letter-spacing:3px;}
.hero-sub{left:87px;top:655px;font-size:16px;line-height:30px;}
.tagline{left:0;top:950px;width:1200px;text-align:center;font-size:25px;font-weight:700;line-height:44px;}

.pill{position:absolute;width:234px;height:97px;display:flex;align-items:center;justify-content:center;text-align:center;font-size:22px;line-height:28px;}
.leave-label{left:453px;top:1260px;width:300px;text-align:center;font-size:32px;font-weight:700;color:var(--blue);}

.values{left:53px;top:1525px;width:1097px;display:flex;}
.value{display:flex;align-items:center;gap:10px;font-size:26px;position:absolute;}

.contact{position:absolute;left:0;width:1200px;height:108px;background:var(--blue);}
.contact--front{top:1591px;}
.contact--back{top:3298px;}
.contact__line{position:absolute;font-size:15px;white-space:nowrap;}
.contact__title{position:absolute;left:480px;top:14px;width:220px;text-align:center;font-size:32px;line-height:40px;color:rgba(255,255,255,.88);letter-spacing:2px;}
.contact svg{position:absolute;}

.testimonials-title{left:660px;top:2042px;width:452px;text-align:center;font-size:48px;letter-spacing:4px;color:var(--blue);}
.quote{position:absolute;left:164px;width:990px;font-size:21px;line-height:29px;letter-spacing:.5px;}
.quote::before{content:"\201C";position:absolute;left:-20px;top:-22px;font-family:var(--serif);font-size:40px;color:var(--quote);}
.quote::after{content:"\201D";position:absolute;right:-2px;bottom:-30px;font-family:var(--serif);font-size:40px;color:var(--quote);}
.footer-name{left:0;top:3215px;width:1200px;text-align:center;font-family:var(--serif);font-size:34px;letter-spacing:1px;color:#2d5d92;}
</style>
</head>
<body>
<div class="canvas">

  <!-- FRONT -->
  <section class="page page--front">
    <svg class="decor" width="1200" height="1591" viewBox="0 0 1200 1591">
      <defs>
        <linearGradient id="handsTone" x1="0" y1="0" x2="1" y2="1">
          <stop offset="0" stop-color="#e8dbd3"/>
          <stop offset=".5" stop-color="#d29a7e"/>
          <stop offset="1" stop-color="#a8755f"/>
        </linearGradient>
      </defs>
      <circle cx="267" cy="560" r="385" fill="none" stroke="#2f6fb0" stroke-width="2"/>
      <path d="M1000 -20 A520 520 0 0 1 1200 290" fill="none" stroke="#2f6fb0" stroke-width="2"/>
      <g role="img" aria-label="Photo of many hands stacked together in a team huddle">
        <circle cx="819" cy="418" r="451" fill="url(#handsTone)"/>
      </g>
      <circle cx="267" cy="585" r="267" fill="var(--blue-soft)" opacity=".93"/>
      <circle cx="1036" cy="819" r="100" fill="var(--navy)" opacity=".85"/>
      <path d="M88 962 L94 974 L88 986 L82 974 Z" fill="var(--blue)"/>

      <!-- leave behind centre -->
      <circle cx="603" cy="1250" r="162" fill="none" stroke="#e8e8e8" stroke-width="3"/>
      <circle cx="603" cy="1250" r="139" fill="var(--light)"/>
      <rect x="573" y="1165" width="8" height="82" fill="#4a6f99"/>
      <path d="M581 1165 H637 L622 1185 L637 1205 H581 Z" fill="#4a6f99"/>

      <!-- pills -->
      <g fill="var(--blue)">
        <rect x="145" y="1083" width="234" height="97" rx="12"/>
        <polygon points="379,1160 390,1184 360,1180"/>
        <rect x="145" y="1217" width="234" height="97" rx="12"/>
        <polygon points="379,1250 397,1265 379,1280"/>
        <rect x="145" y="1352" width="234" height="97" rx="12"/>
        <polygon points="360,1352 390,1344 379,1372"/>
        <rect x="824" y="1083" width="234" height="97" rx="12"/>
        <polygon points="824,1160 813,1184 843,1180"/>
        <rect x="824" y="1217" width="234" height="97" rx="12"/>
        <polygon points="824,1250 806,1265 824,1280"/>
        <rect x="824" y="1352" width="234" height="97" rx="12"/>
        <polygon points="843,1352 813,1344 824,1372"/>
      </g>

      <!-- targets -->
      <g fill="none" stroke="#e6ecf2" stroke-width="3">
        <g transform="translate(110 1135)"><circle r="18"/><circle r="10"/><circle r="3" fill="#e6ecf2"/><path d="M2 -2 L16 -16 M12 -18 L18 -18 L18 -12"/></g>
        <g transform="translate(110 1265)"><circle r="18"/><circle r="10"/><circle r="3" fill="#e6ecf2"/><path d="M2 -2 L16 -16 M12 -18 L18 -18 L18 -12"/></g>
        <g transform="translate(110 1395)"><circle r="18"/><circle r="10"/><circle r="3" fill="#e6ecf2"/><path d="M2 -2 L16 -16 M12 -18 L18 -18 L18 -12"/></g>
        <g transform="translate(1093 1135)"><circle r="18"/><circle r="10"/><circle r="3" fill="#e6ecf2"/><path d="M2 -2 L16 -16 M12 -18 L18 -18 L18 -12"/></g>
        <g transform="translate(1093 1265)"><circle r="18"/><circle r="10"/><circle r="3" fill="#e6ecf2"/><path d="M2 -2 L16 -16 M12 -18 L18 -18 L18 -12"/></g>
        <g transform="translate(1093 1395)"><circle r="18"/><circle r="10"/><circle r="3" fill="#e6ecf2"/><path d="M2 -2 L16 -16 M12 -18 L18 -18 L18 -12"/></g>
      </g>

      <line x1="53" y1="1492" x2="1150" y2="1492" stroke="var(--line)" stroke-width="2"/>

      <!-- value checks -->
      <g fill="none" stroke="var(--blue)" stroke-width="3">
        <g transform="translate(104 1546)"><circle r="14"/><path d="M-6 0 L-1 6 L9 -6"/></g>
        <g transform="translate(349 1546)"><circle r="14"/><path d="M-6 0 L-1 6 L9 -6"/></g>
        <g transform="translate(656 1546)"><circle r="14"/><path d="M-6 0 L-1 6 L9 -6"/></g>
        <g transform="translate(906 1546)"><circle r="14"/><path d="M-6 0 L-1 6 L9 -6"/></g>
      </g>
    </svg>

    <div class="abs brand"><span class="brand__dot"></span>Copper Lantern Gatherings</div>
    <h1 class="abs hero-title">Copper<br>Lantern<br>Gatherings</h1>
    <p class="abs hero-sub">Runs empowerment retreats<br>and bespoke corporate training<br>in creating positive change</p>
    <p class="abs tagline">Our empowerment retreats help people to live without limits,<br>be fierce and wild, be creative and courageous, be fearless and free.</p>

    <div class="pill" style="left:145px;top:1083px;">old fears and<br>beliefs</div>
    <div class="pill" style="left:145px;top:1217px;">old habits</div>
    <div class="pill" style="left:145px;top:1352px;">comfort zone</div>
    <div class="pill" style="left:824px;top:1083px;">lack of<br>self esteem</div>
    <div class="pill" style="left:824px;top:1217px;font-size:19px;line-height:24px;">lack of personal<br>power</div>
    <div class="pill" style="left:824px;top:1352px;">lack of focus</div>
    <p class="abs leave-label">leave behind</p>

    <span class="value" style="left:133px;top:1528px;">Trust</span>
    <span class="value" style="left:378px;top:1528px;">Commitment</span>
    <span class="value" style="left:685px;top:1528px;">Bravery</span>
    <span class="value" style="left:935px;top:1528px;">Flexibility</span>
  </section>

  <div class="contact contact--front">
    <svg width="44" height="34" viewBox="0 0 44 34" style="left:26px;top:12px;" fill="none" stroke="#fff" stroke-width="2"><path d="M2 6 H36 V30 H2 Z M2 6 L19 20 L36 6"/></svg>
    <svg width="44" height="34" viewBox="0 0 44 34" style="left:26px;top:60px;" fill="none" stroke="#fff" stroke-width="2"><rect x="2" y="4" width="34" height="22" rx="2"/><circle cx="32" cy="24" r="7"/><path d="M37 29 L42 33"/></svg>
    <span class="contact__line" style="left:100px;top:19px;">info@copperlanterngatherings.example.com</span>
    <span class="contact__line" style="left:100px;top:66px;">www.copperlanterngatherings.example.co.uk</span>
    <div class="contact__title">Contact<br>Us</div>
    <svg width="84" height="84" viewBox="0 0 84 84" style="left:762px;top:12px;" fill="none" stroke="#fff" stroke-width="3"><path d="M12 14 C4 22 8 46 26 62 C42 76 60 80 68 72 L60 60 L48 64 C40 58 30 48 24 36 L30 24 Z"/><rect x="42" y="6" width="36" height="24" rx="5"/><path d="M50 30 L46 38 L56 30"/><circle cx="52" cy="18" r="1.5" fill="#fff"/><circle cx="60" cy="18" r="1.5" fill="#fff"/><circle cx="68" cy="18" r="1.5" fill="#fff"/></svg>
    <span class="contact__line" style="left:861px;top:19px;">Rebecca Thornby Tel: 07700 900 318</span>
    <span class="contact__line" style="left:861px;top:66px;">Joanna Pelling Tel: 07700 900 752</span>
  </div>

  <!-- BACK -->
  <section class="page page--back">
    <svg class="decor" width="1200" height="1599" viewBox="0 0 1200 1599">
      <defs>
        <linearGradient id="teamTone" x1="0" y1="0" x2="1" y2="1">
          <stop offset="0" stop-color="#7f8fa6"/>
          <stop offset=".5" stop-color="#c9ccd2"/>
          <stop offset="1" stop-color="#8a7f78"/>
        </linearGradient>
      </defs>
      <path d="M1100 0 A480 480 0 0 1 1195 470" fill="none" stroke="#2f6fb0" stroke-width="2"/>
      <g role="img" aria-label="Photo of a smiling team joining hands in a high five around an office table">
        <circle cx="451" cy="354" r="351" fill="url(#teamTone)"/>
      </g>
      <circle cx="886" cy="430" r="226" fill="#ececec" opacity=".96"/>
      <circle cx="735" cy="605" r="100" fill="#3b6fb0" opacity=".88"/>
      <g fill="none" stroke="var(--blue)" stroke-width="3">
        <rect x="853" y="428" width="66" height="46" rx="6"/>
        <path d="M866 474 L862 488 L878 474"/>
        <path d="M864 442 H908 M864 452 H900 M864 462 H890"/>
        <path d="M851 503 l4 9 10 1 -7 6 2 10 -9 -5 -9 5 2 -10 -7 -6 10 -1 Z"/>
        <path d="M878 503 l4 9 10 1 -7 6 2 10 -9 -5 -9 5 2 -10 -7 -6 10 -1 Z"/>
        <path d="M905 503 l4 9 10 1 -7 6 2 10 -9 -5 -9 5 2 -10 -7 -6 10 -1 Z"/>
      </g>
      <g fill="none" stroke="var(--quote)" stroke-width="2.5">
        <g transform="translate(89 792)"><circle r="26"/><circle r="19"/><circle cy="-5" r="7"/><path d="M-12 14 C-10 4 10 4 12 14"/></g>
        <g transform="translate(89 909)"><circle r="26"/><circle r="19"/><circle cy="-5" r="7"/><path d="M-12 14 C-10 4 10 4 12 14"/></g>
        <g transform="translate(89 1033)"><circle r="26"/><circle r="19"/><circle cy="-5" r="7"/><path d="M-12 14 C-10 4 10 4 12 14"/></g>
        <g transform="translate(89 1151)"><circle r="26"/><circle r="19"/><circle cy="-5" r="7"/><path d="M-12 14 C-10 4 10 4 12 14"/></g>
        <g transform="translate(89 1268)"><circle r="26"/><circle r="19"/><circle cy="-5" r="7"/><path d="M-12 14 C-10 4 10 4 12 14"/></g>
        <g transform="translate(89 1385)"><circle r="26"/><circle r="19"/><circle cy="-5" r="7"/><path d="M-12 14 C-10 4 10 4 12 14"/></g>
      </g>
      <line x1="53" y1="1479" x2="1150" y2="1479" stroke="var(--line)" stroke-width="2"/>
    </svg>

    <p class="quote" style="top:777px;">Do not hesitate, just book it!  It will transform and enhance your life.</p>
    <p class="quote" style="top:895px;">If you have a chance to do it then do it, it's one of the best experience of my life.</p>
    <p class="quote" style="top:1017px;">The most wonderful weekend of self-discovery and would recommend it to everyone.</p>
    <p class="quote" style="top:1123px;">I've met the most amazing people and feel like I am well equipped with the tools now to help myself physically and mentally.  The best self-care I've ever invested in.</p>
    <p class="quote" style="top:1240px;">It's changed my life, given me perspective and time to develop myself. I've met the most amazing people and learnt so much.  It's worth every penny.</p>
    <p class="quote" style="top:1358px;">I can't thank Copper Lantern enough for the tools they have metaphorically equipped me with.  They are amazing at what they do.</p>
  </section>

  <p class="abs testimonials-title">Testimonials</p>
  <p class="abs footer-name">Copper Lantern Gatherings</p>

  <div class="contact contact--back">
    <svg width="44" height="34" viewBox="0 0 44 34" style="left:26px;top:12px;" fill="none" stroke="#fff" stroke-width="2"><path d="M2 6 H36 V30 H2 Z M2 6 L19 20 L36 6"/></svg>
    <svg width="44" height="34" viewBox="0 0 44 34" style="left:26px;top:60px;" fill="none" stroke="#fff" stroke-width="2"><rect x="2" y="4" width="34" height="22" rx="2"/><circle cx="32" cy="24" r="7"/><path d="M37 29 L42 33"/></svg>
    <span class="contact__line" style="left:100px;top:22px;">info@copperlanterngatherings.example.com</span>
    <span class="contact__line" style="left:100px;top:69px;">www.copperlanterngatherings.example.co.uk</span>
    <div class="contact__title">Contact<br>Us</div>
    <svg width="84" height="84" viewBox="0 0 84 84" style="left:762px;top:12px;" fill="none" stroke="#fff" stroke-width="3"><path d="M12 14 C4 22 8 46 26 62 C42 76 60 80 68 72 L60 60 L48 64 C40 58 30 48 24 36 L30 24 Z"/><rect x="42" y="6" width="36" height="24" rx="5"/><path d="M50 30 L46 38 L56 30"/><circle cx="52" cy="18" r="1.5" fill="#fff"/><circle cx="60" cy="18" r="1.5" fill="#fff"/><circle cx="68" cy="18" r="1.5" fill="#fff"/></svg>
    <span class="contact__line" style="left:861px;top:22px;">Rebecca Thornby Tel: 07700 900 318</span>
    <span class="contact__line" style="left:861px;top:69px;">Joanna Pelling Tel: 07700 900 752</span>
  </div>

</div>
</body>
</html>
```